Dental Practice Billboard Design

We are a newer dental practice in need of a simple but appealing billboard for our growing dental practice to attract new patients. The practice is owned by husband and wife dentists and is family friendly in a small town in Kentucky. We try to be very friendly and caring to our patients. Would prefer a blue background for the billboard and our tooth logo to be prominent. We are partial to the Patua One font used in the image below but please feel free to tweak it as you deem necessary. The shape of the uppercase D and lowercase g are why we like that font, so fonts with a similarly shaped “D” and “g” would work as well. Please include our phone number (606) 847-3962. Please see our website Harlowfamilydentistry.com for more info on the practice if needed. Thank you! Looking forward to seeing your creation.
Updates

The dimensions will be 12ft x 24ft (3.6576m x 7.3152m). Apologies for not including this in the original prompt. Thank you all for your submissions.

Industry/Entity Type

Dental

Font styles to use
Other font styles liked:
• Patua One

Colors
0054AA
0677BA
7BADD7
CADEEF
E8F1F8
0094D4
00A9DD
6FCCEA
C7EBF8
E9F6FB
00AB8E
00BBA5
67D7C9
C6EFE9
E9F9F6
59FF00
82FF00
B8FF75
E3FFCB
F4FFEA

Requirements
Must have
• Phone number, website, Logo, Practice name “Harlow Family Dentistry”
Should not have
• A tagline or slogan

```html
<!DOCTYPE html>
<html lang="en">
<head>
<meta charset="utf-8">
<title>Harlow Family Dentistry Billboard</title>
<link href="https://fonts.googleapis.com/css2?family=Patua+One&display=swap" rel="stylesheet">
<style>
  :root {
    --navy: #1d4a8c;
    --brand-blue: #3b5fa1;
    --green: #2aa84a;
    --green-light: #6bbd45;
    --white: #ffffff;
    --stage: #e8f1f8;
    --photo-top: #e9ecf2;
    --photo-mid: #c9a48a;
    --photo-low: #dfe4ee;
  }
  * { margin: 0; padding: 0; box-sizing: border-box; }
  html, body { width: 1200px; height: 900px; overflow: hidden; }
  body { background: var(--stage); font-family: "Patua One", Georgia, serif; }

  .billboard {
    position: absolute; left: 40px; top: 170px;
    width: 1120px; height: 560px;
    background: var(--white); overflow: hidden;
    box-shadow: 0 6px 24px rgba(0,0,0,.15);
  }
  .billboard-backdrop { position: absolute; inset: 0; width: 1120px; height: 560px; }

  .team-photo {
    position: absolute; left: 90px; top: 120px; width: 380px; height: 440px;
    background: linear-gradient(180deg, var(--photo-mid) 0%, var(--photo-mid) 25%, var(--photo-top) 45%, var(--photo-low) 100%);
    border-radius: 190px 190px 0 0;
  }

  .brand-lockup {
    position: absolute; left: 520px; top: 48px;
    display: flex; align-items: center; gap: 22px;
    color: var(--brand-blue);
  }
  .brand-mark { width: 96px; height: 96px; border-radius: 50%; background: var(--brand-blue); flex: none; }
  .brand-name { line-height: 1; }
  .brand-name .name-main { display: block; font-size: 78px; }
  .brand-name .name-sub { display: block; font-size: 38px; margin-top: 6px; }

  .headline {
    position: absolute; left: 470px; top: 210px;
    font-size: 86px; font-weight: 400; line-height: 1; white-space: nowrap;
  }
  .headline .word-family { color: var(--navy); }
  .headline .word-dentistry { color: var(--green); }

  .call-band {
    position: absolute; left: 440px; top: 338px; width: 680px; height: 96px;
    background: linear-gradient(90deg, var(--green), var(--green-light));
    border-radius: 30px 0 0 30px;
    display: flex; align-items: center; padding-left: 34px;
    color: var(--white); font-size: 64px; white-space: nowrap;
  }

  .website {
    position: absolute; left: 484px; top: 464px;
    display: flex; align-items: center; gap: 12px;
    color: var(--navy); font-size: 32px; white-space: nowrap;
  }
  .website svg { width: 30px; height: 30px; flex: none; }
</style>
</head>
<body>
  <main class="billboard">
    <svg class="billboard-backdrop" viewBox="0 0 1120 560" aria-hidden="true">
      <defs>
        <linearGradient id="sideGreen" x1="0" y1="0" x2="0" y2="1">
          <stop offset="0" stop-color="#2aa84a"/>
          <stop offset="1" stop-color="#6bbd45"/>
        </linearGradient>
      </defs>
      <rect x="0" y="0" width="260" height="560" fill="url(#sideGreen)"/>
      <path d="M70 0 H480 C405 80 400 300 460 560 H130 C75 420 58 220 70 0 Z" fill="#1d4a8c"/>
    </svg>

    <div class="team-photo" role="img" aria-label="Photo of the two dentists, a woman and a man in white coats, smiling"></div>

    <div class="brand-lockup">
      <span class="brand-mark" aria-hidden="true"></span>
      <div class="brand-name">
        <span class="name-main">Harlow</span>
        <span class="name-sub">Family Dentistry</span>
      </div>
    </div>

    <h1 class="headline"><span class="word-family">Family</span> <span class="word-dentistry">Dentistry</span></h1>

    <div class="call-band">CALL : (606) 847-3962</div>

    <div class="website">
      <svg viewBox="0 0 24 24" aria-hidden="true"><path d="M3 3 L10 21 L12.5 13.5 L20 20 L21.5 18.5 L14.5 12 L21 10 Z" fill="#1d4a8c"/></svg>
      <span>www.harlowfamilydentistry.com</span>
    </div>
  </main>
</body>
</html>
```